Manuka Honey company needs a Upmarket, Luxury Website!

New Zealand, Taranaki based Manuka Honey company Marumaru Honey is looking for a new website, we are looking for an upmarket, luxury, serious website design. We export the highest quality quality Manuka Honey, straight from the Taranaki region.

Main export markets are Asia & Europe, also New Zealand & Australia.

Looking to have a beautiful, upmarket, serious, luxurious & graphical experience with mobile optimization in mind. Like the use of product staging/mockups

You can use copy from other websites to build the site and we will change the copy after the design is finished.

***Please include 'Honey Product' mockups in website.

*Will add illustrator files in coming days***

Feel free to make website functional in Shopify, Wordpress or WIX

Target Market(s)

Asia, Europe (main markets) New Zealand, Australia (Submarkets)

Coding

Coded - Design and coding required

Number of Pages Required

4 page

Requirements
Must have
• Home, Shop, About Us, Contact Us

Homepage to include:

Our Products
Company Video (video under construction)
What is MGO/UMF
Newsletter Opt-in

***(Not in Order)***

Please include 'Honey Product' mockups in website.
*Will add illustrator files in coming days
Nice to have
• FAQ & Partnership Inquiries (hyperlink in footer)

```html
<!DOCTYPE html>
<html lang="en">
<head>
<meta charset="utf-8">
<title>Marumaru Honey</title>
<link rel="stylesheet" href="https://fonts.googleapis.com/css2?family=IBM+Plex+Sans:wght@500;600;700&family=Lato:wght@300;400;700&display=swap">
<style>
:root{
  --purple:#4b1577;
  --purple-deep:#3f1066;
  --gold:#b8900f;
  --gold-bright:#c99a12;
  --ink:#222;
  --muted:#8a8a8a;
  --dark:#1f1d1a;
  --white:#fff;
}
*{box-sizing:border-box;margin:0;padding:0}
html,body{width:1200px;height:3659px;overflow:hidden}
body{position:relative;font-family:"Lato",sans-serif;color:var(--ink);background:var(--white)}
.abs{position:absolute}
a{color:inherit;text-decoration:none}

/* header */
.site-header{left:0;top:0;width:1200px;height:134px;background:var(--white)}
.brand{left:112px;top:28px;width:190px;display:flex;flex-direction:column;align-items:center;gap:8px}
.brand-mark{width:44px;height:44px;border-radius:50%;background:var(--purple)}
.brand-name{font-family:"Lato",sans-serif;font-weight:400;font-size:19px;letter-spacing:3px;color:#333;white-space:nowrap}
.contact-bar{right:112px;top:30px;display:flex;gap:28px;font-size:14px;color:#222}
.contact-bar span{display:flex;align-items:center;gap:6px}
.main-nav{right:112px;top:88px;display:flex;gap:30px;font-size:14px;color:#222}
.main-nav .active{color:var(--purple)}
.main-nav .cart{display:flex;align-items:center;gap:4px}

/* hero */
.hero{left:0;top:134px;width:1200px;height:728px;background:radial-gradient(ellipse at 55% 45%,#7a6a52 0%,#4e4234 45%,#2d271f 100%)}
.hero-title{left:0;width:1200px;top:388px;text-align:center;font-family:"IBM Plex Sans",sans-serif;font-weight:600;font-size:58px;color:var(--white)}
.hero-text{left:270px;width:660px;top:466px;text-align:center;font-size:15px;line-height:34px;color:var(--white)}
.btn{display:flex;align-items:center;justify-content:center;background:var(--gold);color:var(--white);font-size:15px;font-weight:400;letter-spacing:.5px}
.hero-btn{left:531px;top:547px;width:155px;height:51px;color:#3b2a08}
.dots{display:flex;gap:8px}
.dot{width:15px;height:15px;border-radius:50%;border:1.5px solid #fff}
.dot.on{background:#fff}
.hero-dots{left:558px;top:824px}
.dark-dots .dot{border-color:#222}
.dark-dots .dot.on{background:#222}

/* headings */
.section-title{left:0;width:1200px;text-align:center;font-family:"IBM Plex Sans",sans-serif;font-weight:600;font-size:32px;color:var(--ink)}
.rule{height:4px;background:var(--purple)}

/* products */
.products{left:0;top:862px;width:1200px;height:683px;background:linear-gradient(180deg,#fff 60%,#f4f1ec 100%)}
.product-card{top:1042px;width:319px;height:257px;background:var(--white);border:2px solid #e6e6e6;box-shadow:0 2px 6px rgba(0,0,0,.08)}
.jar{position:absolute;left:104px;top:46px;width:110px;height:190px;border-radius:18px 18px 22px 22px}
.jar-gold{background:linear-gradient(90deg,#c8850c,#f2b325 50%,#c8850c)}
.jar-amber{background:linear-gradient(90deg,#d8560c,#f47c1e 50%,#d8560c)}
.jar-yellow{background:linear-gradient(90deg,#e0a000,#ffcf1c 50%,#e0a000)}
.card-cart{position:absolute;right:26px;top:26px}
.product-name{top:1324px;width:319px;text-align:center;font-family:"IBM Plex Sans",sans-serif;font-weight:600;font-size:14px;letter-spacing:.3px}
.product-price{top:1355px;width:319px;text-align:center;font-size:15px;font-weight:700;color:var(--gold)}
.arrow{top:1158px}

/* video */
.video{left:0;top:1545px;width:1200px;height:667px;background:linear-gradient(90deg,#1c1a17,#2a2520 60%,#4a3f30)}
.video-frame{left:112px;top:1684px;width:977px;height:464px;border:2px solid var(--gold);background:linear-gradient(120deg,#3a3f48 0%,#5a4c3e 40%,#c97a22 62%,#6b4a2a 85%,#2f2f33 100%)}
.play{left:571px;top:1888px}

/* mgo */
.mgo{left:0;top:2212px;width:1200px;height:658px;background:linear-gradient(180deg,#fff 60%,#f6f3ee 100%)}
.mgo-title{left:111px;top:2332px;font-family:"IBM Plex Sans",sans-serif;font-weight:600;font-size:31px}
.mgo-text{left:113px;top:2414px;width:450px;font-size:14.5px;font-weight:300;line-height:34.3px;color:var(--muted)}
.mgo-btn{left:112px;top:2680px;width:155px;height:51px;color:#3b2a08}
.mgo-frame{left:572px;top:2332px;width:500px;height:437px;border:1.5px solid #b79a6a}
.mgo-photo{left:591px;top:2316px;width:497px;height:435px;background:linear-gradient(110deg,#3d5a2c 0%,#6a8a48 35%,#dad7cf 55%,#c9b23a 85%,#e0c424 100%);box-shadow:0 4px 12px rgba(0,0,0,.15)}

/* newsletter */
.newsletter{left:0;top:2870px;width:1200px;height:386px;background:linear-gradient(180deg,#1c1b19,#24221d)}
.news-title{left:0;width:1200px;top:2948px;text-align:center;font-family:"Lato",sans-serif;font-weight:400;font-size:31px;color:var(--gold-bright)}
.field{top:3026px;width:317px;height:56px;background:var(--white);font-size:16px;color:#333;padding:18px 16px}
.submit{left:459px;top:3120px;width:282px;height:50px;border-radius:25px;color:var(--purple-deep)}

/* footer */
.site-footer{left:0;top:3256px;width:1200px;height:403px;background:var(--purple)}
.foot-col{top:3334px;color:var(--white)}
.foot-col h3{font-family:"Lato",sans-serif;font-weight:700;font-size:15px;margin-bottom:10px}
.foot-col li{list-style:none;font-size:15px;line-height:34.2px;padding-left:2px}
.foot-col .u{text-decoration:underline}
.socials{left:985px;top:3363px;display:flex;gap:10px}
.socials span{width:18px;height:18px;border-radius:50%;background:var(--white)}
.copyright{left:0;width:1200px;top:3608px;text-align:center;color:var(--white);font-size:15.5px}
</style>
</head>
<body>

<header class="site-header abs">
  <div class="brand abs">
    <span class="brand-mark"></span>
    <span class="brand-name">MARUMARU HONEY</span>
  </div>
  <div class="contact-bar abs">
    <span><svg width="14" height="11" viewBox="0 0 14 11"><rect width="14" height="11" rx="1" fill="#4b1577"/><path d="M1 1l6 5 6-5" stroke="#fff" fill="none" stroke-width="1.2"/></svg>EMAIL NOW - MarumaruHoney.com</span>
    <span><svg width="12" height="12" viewBox="0 0 12 12"><path d="M2 1l2 0 1 3-1.5 1a7 7 0 0 0 3.5 3.5L8 7l3 1v2c0 1-1 1-1 1A9 9 0 0 1 1 2s0-1 1-1z" fill="#4b1577"/></svg>CALL NOW - 123-456-7890</span>
  </div>
  <nav class="main-nav abs">
    <a class="active">HOME</a><a>ABOUT</a><a>PRODUCTS</a><a>VIDEO</a><a>FAQ</a><a>CONTACT</a>
    <a class="cart"><svg width="15" height="13" viewBox="0 0 15 13"><path d="M0 1h3l2 7h8l2-6H4" fill="#222"/><circle cx="6" cy="11" r="1.5" fill="#222"/><circle cx="12" cy="11" r="1.5" fill="#222"/></svg>CART(0)</a>
  </nav>
</header>

<section class="hero abs" role="img" aria-label="Close-up of honey bees swarming on a hive"></section>
<h1 class="hero-title abs">MARUMARU HONEY</h1>
<p class="hero-text abs">Lorem ipsum dolor sit amet, consectetur adipiscing elit, sed do eiusmod tempor incididunt ut labore et dolore magna aliqua</p>
<a class="btn hero-btn abs">ORDER NOW</a>
<div class="dots hero-dots abs"><span class="dot on"></span><span class="dot"></span><span class="dot"></span><span class="dot"></span></div>

<section class="products abs"></section>
<h2 class="section-title abs" style="top:954px">OUR PRODUCTS</h2>
<div class="rule abs" style="left:557px;top:1006px;width:86px"></div>

<svg class="arrow abs" style="left:86px" width="16" height="26" viewBox="0 0 16 26"><path d="M13 2L3 13l10 11" stroke="#222" stroke-width="3" fill="none"/></svg>
<svg class="arrow abs" style="left:1100px" width="16" height="26" viewBox="0 0 16 26"><path d="M3 2l10 11L3 24" stroke="#222" stroke-width="3" fill="none"/></svg>

<div class="product-card abs" style="left:111px">
  <div class="jar jar-gold" role="img" aria-label="Jar of golden manuka honey"></div>
  <svg class="card-cart" width="18" height="16" viewBox="0 0 15 13"><path d="M0 1h3l2 7h8l2-6H4" fill="#4b1577"/><circle cx="6" cy="11" r="1.5" fill="#4b1577"/><circle cx="12" cy="11" r="1.5" fill="#4b1577"/></svg>
</div>
<div class="product-card abs" style="left:440px">
  <div class="jar jar-amber" role="img" aria-label="Jar of amber manuka honey"></div>
  <svg class="card-cart" width="18" height="16" viewBox="0 0 15 13"><path d="M0 1h3l2 7h8l2-6H4" fill="#4b1577"/><circle cx="6" cy="11" r="1.5" fill="#4b1577"/><circle cx="12" cy="11" r="1.5" fill="#4b1577"/></svg>
</div>
<div class="product-card abs" style="left:770px">
  <div class="jar jar-yellow" role="img" aria-label="Jar of light manuka honey"></div>
  <svg class="card-cart" width="18" height="16" viewBox="0 0 15 13"><path d="M0 1h3l2 7h8l2-6H4" fill="#4b1577"/><circle cx="6" cy="11" r="1.5" fill="#4b1577"/><circle cx="12" cy="11" r="1.5" fill="#4b1577"/></svg>
</div>
<p class="product-name abs" style="left:111px">LOREM IPSUM DOLOR SIT AMET</p>
<p class="product-name abs" style="left:440px">LOREM IPSUM DOLOR SIT AMET</p>
<p class="product-name abs" style="left:770px">LOREM IPSUM DOLOR SIT AMET</p>
<p class="product-price abs" style="left:111px">$150.00</p>
<p class="product-price abs" style="left:440px">$150.00</p>
<p class="product-price abs" style="left:770px">$150.00</p>
<div class="dots dark-dots abs" style="left:558px;top:1428px"><span class="dot on"></span><span class="dot"></span><span class="dot"></span><span class="dot"></span></div>

<section class="video abs"></section>
<h2 class="section-title abs" style="top:1596px;color:#fff">OUR VIDEO</h2>
<div class="rule abs" style="left:557px;top:1648px;width:86px;background:#fff"></div>
<div class="video-frame abs" role="img" aria-label="Honey dripping from a dipper into a cup of tea with lemon slices"></div>
<svg class="play abs" width="56" height="56" viewBox="0 0 56 56"><circle cx="28" cy="28" r="28" fill="#fff"/><path d="M22 17l17 11-17 11z" fill="#222"/></svg>

<section class="mgo abs"></section>
<h2 class="mgo-title abs">WHAT IS MGO/UMF</h2>
<div class="rule abs" style="left:112px;top:2384px;width:86px"></div>
<p class="mgo-text abs">Lorem ipsum dolor sit amet, consectetur adipiscing elit, sed do eiusmod tempor incididunt ut labore et dolore magna aliqua. Ut enim ad minim veniam, quis nostrud exercitation ullamco laboris nisi ut aliquip ex ea commodo consequat. Duis aute irure dolor in reprehenderit in voluptate velit esse cillum dolore eu fugiat nulla pariatur. Excepteur sint occaecat cupidatat non proident, sunt in culpa qui officia deserunt mollit anim id est laborum</p>
<a class="btn mgo-btn abs">READ MORE</a>
<div class="mgo-frame abs"></div>
<div class="mgo-photo abs" role="img" aria-label="Beekeeper in protective suit tending yellow hives in a green field"></div>

<section class="newsletter abs"></section>
<h2 class="news-title abs">NEWSLETTER SUBSCRIBE</h2>
<div class="field abs" style="left:112px">Name</div>
<div class="field abs" style="left:442px">Email</div>
<div class="field abs" style="left:772px">Phone</div>
<a class="btn submit abs">SUBMIT NOW</a>

<footer class="site-footer abs"></footer>
<div class="foot-col abs" style="left:111px"><h3>PRODUCTS</h3><ul><li>Lorem ipsum dolor</li><li>Lorem ipsum dolor</li><li>Lorem ipsum dolor</li><li>Lorem ipsum dolor</li></ul></div>
<div class="foot-col abs" style="left:362px"><h3>ABOUT</h3><ul><li>About Us</li><li>Team</li><li>Terms &amp; conditions</li><li>Privacy Policy</li><li>Review</li></ul></div>
<div class="foot-col abs" style="left:596px;top:3336px"><h3>QUICK LINKS</h3><ul><li>Home</li><li>About</li><li>Products</li><li>Video</li><li>Contact</li></ul></div>
<div class="foot-col abs" style="left:775px;top:3336px"><h3>HELP</h3><ul><li>Information</li><li>Support</li><li class="u">FAQ</li></ul></div>
<div class="socials abs"><span></span><span></span><span></span><span></span></div>
<p class="copyright abs">© 2021&nbsp; All Rights Reserved</p>

</body>
</html>
```